One page company profile for exclusive wine import

Valtrenor is an importer of exclusive, rare wines into indonesia. We would like a stylish, classy, upmarket but professional one pager containing our company profile.

Please include the text we prepared (see must haves) and read through it to get a better understanding of what our company is doing

We would like the one pager to have a dark background, and contain a drawing or drawing-style picture related to wine and/or global import (see examples). We would like to have it in PDF as well as in a word-template so we can later produce translations and/or adaptations to the text.

Target Market(s)

The one pagers is directed to distributors and upmarket hotels and restaurants.

Requirements
Must have
• We would like the one pager to have a dark background, and contain a drawing or drawing-style picture related to wine and/or global import (see examples)
• Our logo (see files) on the one pager
• The following contact details: E-mail: info@valtrenor-example.eu
• Word template and PDF
• The following text:
• "Valtrenor brings rare, exceptional wines to the Indonesian market. We
• specialize in French and Italian wines that even in Europe are very hard
• to get by. We have an extensive network of big and small, famous and less
• known winemakers that reserve a portion of their production for us.
• Together with them, we supply the market with an excellent range of the
• absolute best European wines.
• We buy our products directly at the winemaker in France or Italy Through a
• licensed importer, the wines are brought to Indonesia by airfreight and
• stored in air-conditioned, optimal conditions, awaiting distribution to
• our customers. All of this ensured that the wine loses none of its quality
• during transport from the winemaker to the customer.
• We always look out for partners that are eager to distribute or retail.
• Our intentions working with them are always to work on a long term basis.
• With these intentions we see that both sides together have to engage
• themselves to succeed in sales and establishing brand recognition in the
• Indonesian market. Our philosophy is based on trust, responsibility,
• mutual respect and of course a love for great wine!
• We advise our clients on tasting, food pairing, storing and aging the wine
• and provide a technical datasheet with all our bottles. We pride ourselves
• in our customer service and are always available for any enquiry."
Should not have
• clichés like pictures of grapes, vineyards, barrels, etc... (stylised drawings are preferred and allowed)

```html
<!DOCTYPE html>
<html lang="en">
<head>
<meta charset="utf-8">
<title>Valtrenor – Company Profile</title>
<link href="https://fonts.googleapis.com/css2?family=Lato:wght@400;700;900&display=swap" rel="stylesheet">
<style>
  :root{
    --navy:#16224a;
    --red:#e31b23;
    --ice:#d6eefa;
    --white:#ffffff;
    --stage:#dcdcdc;
  }
  *{margin:0;padding:0;box-sizing:border-box}
  html,body{width:1200px;height:906px;overflow:hidden;background:var(--stage)}
  body{font-family:"Lato",sans-serif;color:var(--white)}
  .flyer{position:absolute;left:290px;top:14px;width:620px;height:877px;background:var(--navy);overflow:hidden;box-shadow:0 6px 24px rgba(0,0,0,.18)}
  .flyer-shapes{position:absolute;inset:0}
  .block{position:absolute}
  .brand{left:36px;top:30px;display:flex;align-items:center;gap:14px}
  .brand-dot{width:46px;height:46px;border-radius:50%;background:var(--white);flex:none}
  .brand-name{font-weight:900;font-size:36px;letter-spacing:2px;line-height:1;color:var(--white)}
  .intro{left:36px;top:92px;width:340px;font-size:10.5px;line-height:1.45}
  .headline{left:36px;top:180px;width:340px;font-weight:900;font-size:21px;line-height:1.12;text-transform:uppercase}
  .sourcing{left:36px;top:318px;width:340px;font-size:10px;line-height:1.45}
  .partners{left:36px;top:414px;width:360px;font-weight:700;font-size:17px;line-height:1.2}
  .partners p+p{margin-top:8px}
  .philosophy{left:36px;top:516px;width:380px;font-size:10px;line-height:1.45}
  .service{left:36px;top:618px;width:330px;font-size:10px;line-height:1.45;color:var(--navy)}
  .service-badge{left:400px;top:624px;width:190px;height:46px;background:var(--white);border-radius:12px;display:flex;align-items:center;justify-content:center;gap:8px}
  .service-badge .brand-dot{width:22px;height:22px;background:var(--red)}
  .service-badge .brand-name{font-size:22px;letter-spacing:1.5px;color:var(--navy)}
  .phone{left:36px;top:716px;font-weight:900;font-size:30px;letter-spacing:1px}
  .website{left:36px;top:806px;font-weight:900;font-size:20px}
  .wine-illustration{left:466px;top:200px;width:136px;height:270px;border-radius:40% 40% 30% 30%;background:radial-gradient(ellipse at 45% 35%,var(--red) 0%,#c2202c 45%,rgba(22,34,74,.55) 75%,rgba(214,238,250,0) 100%)}
</style>
</head>
<body>
<main class="flyer">
  <svg class="flyer-shapes" width="620" height="877" viewBox="0 0 620 877" aria-hidden="true">
    <rect class="sourcing-band" x="0" y="308" width="620" height="92" fill="var(--red)"/>
    <path class="side-panel" d="M440,0 C380,260 410,500 620,630 L620,0 Z" fill="var(--ice)"/>
    <path class="side-panel-edge" d="M440,0 C380,260 410,500 620,630" fill="none" stroke="var(--red)" stroke-width="6"/>
    <rect class="service-band" x="0" y="604" width="620" height="88" fill="var(--ice)"/>
    <rect class="contact-band" x="0" y="784" width="620" height="93" fill="var(--red)"/>
  </svg>

  <div class="block wine-illustration" role="img" aria-label="Stylised drawing of a wine glass with red wine splashing"></div>

  <header class="block brand">
    <span class="brand-dot"></span>
    <span class="brand-name">VALTRENOR</span>
  </header>

  <p class="block intro">Valtrenor brings rare, exceptional wines to the Indonesian market. We specialize in French and Italian wines that even in Europe are very hard to get by. We have an extensive network of big and small, famous and less known winemakers that reserve a portion of their production for us.</p>

  <h1 class="block headline">Together with them, we supply the market with an excellent range of the absolute best European wines.</h1>

  <p class="block sourcing">We buy our products directly at the winemaker in France or Italy. Through a licensed importer, the wines are brought to Indonesia by airfreight and stored in air-conditioned, optimal conditions, awaiting distribution to our customers. All of this ensures that the wine loses none of its quality during transport from the winemaker to the customer.</p>

  <div class="block partners">
    <p>We always look out for partners that are eager to distribute or retail.</p>
    <p>Our intentions working with them are always to work on a long term basis.</p>
  </div>

  <p class="block philosophy">With these intentions we see that both sides together have to engage themselves to succeed in sales and establishing brand recognition in the Indonesian market. Our philosophy is based on trust, responsibility, mutual respect and of course a love for great wine!</p>

  <p class="block service">We advise our clients on tasting, food pairing, storing and aging the wine and provide a technical datasheet with all our bottles. We pride ourselves in our customer service and are always available for any enquiry.</p>

  <div class="block service-badge">
    <span class="brand-dot"></span>
    <span class="brand-name">VALTRENOR</span>
  </div>

  <p class="block phone">(123) 456 7890</p>
  <p class="block website">yourwebsitehere.com</p>
</main>
</body>
</html>
```